HOPE TABERNACLE- Premier Church Service.

Date: Sunday April 28th 2019.
Time: 10:30am-12:30pm
Venue: Blue Heron Hotel & conference Centre
4 N. Pellman Road Renton Wa 98064 USA.
Special treat at no extra cost!!!!
-Breakfast available 9am-10:15am.

-3 course Lunch available after Church.

NB: AMAZING ARRANGEMENTS FOR CHILDREN.
...........................................................................................................

EVENING JUBILEE, Wa 2019..........6:30pm-8:30pm.
" A time of high praise, deep Worship, the prophetic, Salvation, healing, miracles and more! "

...........................................................................................................................

Resident Pastors: Pastors Lou & Mary Kamau.

Guest ministers:

Apostle Daniel Otieno
Well of Mercy Sacramento, California.

THE LADY IN PINK IS THE WIFE TO THE MAN WITH THE ORANGE CLOTH IN HIS JACKET POSCKET. TRY MAKE IT COME OUT AS IF THESE TWO WERE TAKEN TOGETHER.

16-60

Designer to choose colors to be used in the design.

• -Very catchy and creative design.

```html
<!DOCTYPE html>
<html lang="en">
<head>
<meta charset="utf-8">
<title>Evening Jubilee – Hope Tabernacle</title>
<link rel="stylesheet" href="https://fonts.googleapis.com/css2?family=Russo+One&family=Archivo:ital,wght@1,800&family=Open+Sans:wght@600&family=Arimo:wght@400;700&family=Oswald:wght@600&display=swap">
<style>
  :root {
    --navy: #0d4278;
    --title-navy: #0c3b6e;
    --orange: #f7931e;
    --yellow: #f9c623;
    --green-light: #a8f35c;
    --green: #5fd82c;
    --green-deep: #34b51c;
    --white: #ffffff;
    --ink: #111111;
  }
  * { margin: 0; padding: 0; box-sizing: border-box; }
  html, body { width: 1200px; height: 1200px; overflow: hidden; background: var(--white); }
  .flyer {
    position: absolute; left: 255px; top: 113px; width: 691px; height: 977px;
    overflow: hidden;
    background: radial-gradient(ellipse at 45% 35%, var(--green-light) 0%, var(--green) 45%, var(--green-deep) 100%);
    font-family: "Arimo", Arial, sans-serif;
  }
  .flyer > * { position: absolute; }
  .title {
    left: 0; width: 691px; top: 22px; text-align: center;
    font-family: "Russo One", sans-serif; font-size: 63px; line-height: 1;
    color: var(--title-navy); letter-spacing: -1px;
    transform: scaleY(1.45); transform-origin: top center;
  }
  .time-tag {
    left: 169px; top: 106px; width: 352px; height: 42px;
    background: var(--orange); transform: rotate(-2deg);
    font-family: "Open Sans", sans-serif; font-weight: 600; font-size: 19px;
    color: var(--ink); display: flex; align-items: center; justify-content: center;
  }
  .tagline {
    left: 50px; width: 630px; top: 158px; text-align: center;
    font-family: "Archivo", sans-serif; font-style: italic; font-weight: 800;
    font-size: 31px; line-height: 41px; color: var(--ink);
    text-shadow: 0 0 3px rgba(255,255,255,.8);
  }
  .photo { border-radius: 40% 40% 0 0 / 20% 20% 0 0; }
  .photo-resident {
    left: 17px; top: 291px; width: 345px; height: 400px;
    background: linear-gradient(180deg, #3a3a3a 0%, #9fb3cf 55%, #c7d3e4 100%);
  }
  .photo-guest {
    left: 377px; top: 283px; width: 300px; height: 360px;
    background: linear-gradient(180deg, #2d2d2d 0%, #e23ec8 45%, #b9a08e 100%);
  }
  .waves { left: 0; top: 0; width: 691px; height: 977px; }
  .pastors { right: 31px; top: 610px; text-align: right; color: var(--white); }
  .pastors .label { font-size: 16px; margin-bottom: 4px; }
  .pastors .names { font-weight: 700; font-size: 34px; line-height: 39px; }
  .divider { left: 337px; top: 695px; width: 1px; height: 256px; background: var(--white); }
  .service { left: 0; width: 343px; top: 743px; text-align: center; color: var(--white); }
  .service .date { color: var(--yellow); font-size: 25px; }
  .service .hours { font-size: 20px; margin-top: 12px; }
  .service .venue { font-size: 15px; line-height: 22px; margin-top: 16px; }
  .service .treat {
    font-family: "Oswald", sans-serif; font-weight: 600; color: var(--yellow);
    font-size: 20px; margin-top: 10px;
  }
  .service .meals { font-size: 14px; line-height: 25px; margin-top: 4px; }
  .guests { left: 340px; width: 330px; top: 735px; text-align: center; color: var(--white); }
  .guests .label { text-align: left; padding-left: 15px; font-size: 19px; }
  .guests .minister {
    font-family: "Oswald", sans-serif; font-weight: 600; color: var(--yellow);
    font-size: 25px; margin-top: 8px;
  }
  .guests .church { font-size: 19px; line-height: 28px; margin-top: 4px; }
  .guests .children {
    font-family: "Oswald", sans-serif; font-weight: 600; color: var(--yellow);
    font-size: 25px; line-height: 36px; margin-top: 22px;
  }
</style>
</head>
<body>
  <main class="flyer">
    <h1 class="title">EVENING JUBILEE</h1>
    <div class="time-tag">Wa 2019..........6:30pm-8:30 pm.</div>
    <p class="tagline">A time of high praise, deep Worship, the prophetic, Salvation, healing, miracles and more!</p>

    <div class="photo photo-resident" role="img" aria-label="Photo of resident pastors Lou and Mary Kamau"></div>
    <div class="photo photo-guest" role="img" aria-label="Photo of guest minister Apostle Daniel Otieno with his wife"></div>

    <svg class="waves" viewBox="0 0 691 977" aria-hidden="true">
      <path d="M0 611 C80 670 200 700 300 680 C430 650 560 540 691 551 L691 977 L0 977 Z" fill="var(--orange)"/>
      <path d="M0 683 C120 705 260 700 380 650 C500 600 600 570 691 578 L691 977 L0 977 Z" fill="var(--navy)"/>
    </svg>

    <div class="pastors">
      <p class="label">Resident Pastors</p>
      <p class="names">Pastors Lou<br>&amp; Mary Kamau</p>
    </div>

    <div class="divider"></div>

    <section class="service">
      <p class="date">Sunday I April 28th I 2019</p>
      <p class="hours">10:30am - 12:30pm</p>
      <p class="venue">Blue Heron Hotel &amp; conference Centre<br>4 N. Pellman Road Renton Wa 98064 USA.</p>
      <p class="treat">Special treat at no extra cost!!!!</p>
      <p class="meals">Breakfast available 9am-10:15am.<br>3 course Lunch available after Church.</p>
    </section>

    <section class="guests">
      <p class="label">Guest ministers:</p>
      <p class="minister">Apostle Daniel Otieno</p>
      <p class="church">Well of Mercy Sacramento,<br>California.</p>
      <p class="children">AMAZING ARRANGEMENTS<br>FOR CHILDREN</p>
    </section>
  </main>
</body>
</html>
```